braided hoses

Tue, Jun 25, 3:27 PM (17 hours ago)

WE ARE LOOKING FOR A FLYER WE CAN EMAIL OU TO EXISTING CUSTOMERS - MECHANICAL INDUSTRIAL WHOLESALE ETC

WE SUPPLY PERFORMANCE FITTINGS TO MAKE BRAIDED HOSE FOR RACECAR, ENTHUSIASTS AND GENERAL CARS
these are used for
brake hoses
cooler lines
oil + fuel hoses

pictures supplied but if better pictures found will be ok
i do not want to pay for pictures afterwards

Requirements
Must have
• company details correct

```html
<!DOCTYPE html>
<html lang="en">
<head>
<meta charset="utf-8">
<title>Braided Hoses Flyer – Summit Motor Works</title>
<link rel="stylesheet" href="https://fonts.googleapis.com/css2?family=Anton&family=Bebas+Neue&family=Montserrat:ital,wght@0,500;0,600;0,700;0,800;1,800&family=Oswald:wght@300;500;700&family=Russo+One&display=swap">
<style>
  :root{
    --stage:#2b2b2b;
    --paper:#ffffff;
    --yellow:#f2d000;
    --red:#8e1b1f;
    --red-dark:#6e1316;
    --red-text:#a3202a;
    --ink:#141414;
    --grey:#d7d7d7;
    --card-dark:#1d1d1d;
  }
  *{box-sizing:border-box;margin:0;padding:0}
  html,body{width:1200px;height:1200px;overflow:hidden;background:var(--stage)}
  .flyer{position:absolute;left:204px;top:40px;width:792px;height:1120px;background:var(--paper);overflow:hidden;font-family:"Montserrat",sans-serif;color:var(--ink)}
  .backdrop{position:absolute;inset:0}
  .abs{position:absolute;white-space:nowrap}

  .photo-placeholder{position:absolute}
  .hoses-photo{left:513px;top:233px;width:279px;height:430px;
    background:linear-gradient(160deg,#9a8f78 0%,#5d5546 45%,#8b826d 70%,#3c372e 100%);
    clip-path:polygon(40% 0,100% 0,100% 100%,60% 100%,0 20%)}
  .fitting-photo{left:46px;top:452px;width:264px;height:358px;
    background:linear-gradient(180deg,#2c5ab8 0%,#2c5ab8 38%,#b8262b 38%,#d63a3c 58%,#2c5ab8 58%,#2c5ab8 66%,#b8262b 66%,#8e1b1f 100%);
    clip-path:polygon(0 0,100% 0,100% 136px,131px 136px,131px 100%,0 100%);
    border-radius:30px 10px 10px 26px}

  .kicker{left:46px;top:73px;width:453px;height:44px;background:
      repeating-linear-gradient(135deg,var(--red) 0 5px,var(--red-dark) 5px 7px);
    clip-path:polygon(0 0,100% 0,91% 100%,0 100%);
    font-family:"Bebas Neue",sans-serif;color:#fff;font-size:35px;letter-spacing:.5px;line-height:46px;padding-left:17px}
  .kicker span{display:inline-block;transform:skewX(-10deg)}
  .rule{height:2px;background:var(--ink)}
  .quality{left:48px;top:135px;font-family:"Russo One",sans-serif;font-style:italic;font-size:37px;color:var(--yellow);-webkit-text-stroke:1.5px var(--ink);letter-spacing:1px;line-height:42px}
  .headline{left:46px;top:192px;font-family:"Anton",sans-serif;font-style:italic;font-weight:400;font-size:96px;line-height:101px;color:var(--ink);letter-spacing:-1px}

  .brand{left:538px;top:190px;display:flex;align-items:center;gap:8px}
  .brand-mark{width:14px;height:14px;background:var(--yellow);flex:none}
  .brand-name{font-family:"Oswald",sans-serif;font-weight:500;font-size:21px;line-height:24px;color:var(--ink);text-transform:uppercase}

  .tagline{left:163px;top:604px;width:536px;height:80px;background:
      repeating-linear-gradient(135deg,var(--red) 0 5px,var(--red-dark) 5px 7px);
    clip-path:polygon(0 0,88% 0,100% 100%,0 100%);padding:9px 0 0 46px;font-style:italic;font-weight:800}
  .tagline .lead{color:var(--yellow);font-size:30px;letter-spacing:4px;line-height:34px}
  .tagline .sub{color:#fff;font-size:23px;letter-spacing:4px;line-height:26px}

  .supply-title{left:208px;top:714px;font-weight:500;font-size:16px;letter-spacing:6px}
  .supply-list{left:208px;top:735px;width:517px;height:73px;border-top:2px solid var(--grey);border-bottom:2px solid var(--grey);display:flex}
  .segment{font-weight:800;font-size:27px;line-height:23px;padding-top:14px}
  .segment span{display:block;color:var(--red-text)}
  .segment + .segment{border-left:2px solid var(--grey);padding-left:17px}
  .seg-race{width:109px}
  .seg-enth{width:249px}

  .features{left:62px;top:846px;width:147px;text-align:right;font-family:"Oswald",sans-serif;font-weight:300;font-style:italic;font-size:23px;line-height:24px;letter-spacing:-1px}
  .features li{list-style:none;padding:4px 0}
  .features li + li{border-top:2px solid var(--grey)}

  .use-card{top:840px;width:156px;height:153px;border-radius:18px 18px 0 0;overflow:hidden;
    background:linear-gradient(180deg,var(--card-dark) 0 53%,#e2e2e2 53%,#fff 100%);text-align:center}
  .use-card h3{font-family:"Bebas Neue",sans-serif;font-weight:400;color:#fff;font-size:23px;letter-spacing:.5px;margin-top:10px}
  .use-card .icon{width:60px;height:60px;margin:8px auto 0;border-radius:50%;background:#fff;border:5px solid var(--yellow)}
  .use-card p{font-size:11px;line-height:14px;font-weight:500;margin-top:8px;color:#222}
  .card-brake{left:234px}
  .card-cooler{left:406px}
  .card-fuel{left:576px}

  .call{left:64px;top:1016px;font-weight:700;font-size:22px}
  .web{left:62px;top:1044px;width:296px;height:28px;border-radius:14px;background:var(--red-text);color:#fff;font-size:14px;letter-spacing:2px;text-align:center;line-height:28px;font-weight:500}
  .email{left:389px;top:1020px;width:338px;font-size:16px;font-weight:600;padding-bottom:6px;border-bottom:2px solid var(--grey)}
  .address{left:389px;top:1057px;font-size:13.5px;font-weight:600}
</style>
</head>
<body>
<main class="flyer">
  <svg class="backdrop" width="792" height="1120" viewBox="0 0 792 1120" aria-hidden="true">
    <defs>
      <pattern id="pinstripe" width="14" height="14" patternUnits="userSpaceOnUse" patternTransform="rotate(45)">
        <rect width="14" height="14" fill="#ececec"/>
        <rect width="6" height="14" fill="#f7f7f7"/>
      </pattern>
      <linearGradient id="yellowTone" x1="0" y1="0" x2="1" y2="1">
        <stop offset="0" stop-color="#e9c800"/>
        <stop offset="1" stop-color="#f7da10"/>
      </linearGradient>
      <linearGradient id="workshopTone" x1="0" y1="0" x2="0" y2="1">
        <stop offset="0" stop-color="#9a9a9a"/>
        <stop offset="1" stop-color="#3a3a3a"/>
      </linearGradient>
    </defs>
    <polygon points="528,0 792,0 792,800 640,800" fill="url(#pinstripe)"/>
    <polygon points="449,129 792,640 792,720 240,720" fill="#d9d9d9"/>
    <polygon points="0,0 528,0 0,817" fill="url(#yellowTone)" role="img" aria-label="Yellow-toned workshop photograph"/>
    <polygon points="429,258 633,575 225,575" fill="url(#workshopTone)" role="img" aria-label="Photograph of hands assembling a hose fitting in a workshop"/>
  </svg>

  <div class="photo-placeholder hoses-photo" role="img" aria-label="Photograph of four braided steel hoses"></div>
  <div class="photo-placeholder fitting-photo" role="img" aria-label="Photograph of a red and blue 90-degree hose fitting"></div>

  <div class="abs kicker"><span>PERFORMANCE FITTINGS FOR</span></div>
  <div class="abs rule" style="left:46px;top:129px;width:334px"></div>
  <div class="abs quality">TOP-QUALITY</div>
  <div class="abs rule" style="left:46px;top:181px;width:328px"></div>
  <h1 class="abs headline">BRAIDED<br>HOSES</h1>

  <div class="abs brand">
    <span class="brand-mark"></span>
    <span class="brand-name">Summit Motor Works</span>
  </div>

  <div class="abs tagline">
    <div class="lead">ENHANCE YOUR</div>
    <div class="sub">VEHICLE'S PERFORMANCE</div>
  </div>

  <div class="abs supply-title">WE SUPPLY FITTINGS FOR:</div>
  <div class="abs supply-list">
    <div class="segment seg-race">RACE<span>CARS</span></div>
    <div class="segment seg-enth">ENTHUSIASTS'<span>VEHICLES</span></div>
    <div class="segment">GENERAL<span>CARS</span></div>
  </div>

  <ul class="abs features">
    <li>HIGH<br>PERFORMANCE</li>
    <li>WIDE RANGE</li>
    <li>EXPERT SUPPORT</li>
  </ul>

  <section class="abs use-card card-brake">
    <h3>BRAKE HOSES</h3>
    <div class="icon">
      <svg width="50" height="50" viewBox="0 0 50 50" aria-hidden="true"><path d="M15 12v18a5 5 0 0 0 10 0V20a5 5 0 0 1 10 0v18" fill="none" stroke="#111" stroke-width="3" stroke-linecap="round"/></svg>
    </div>
    <p>Ensuring reliable<br>and safe braking</p>
  </section>
  <section class="abs use-card card-cooler">
    <h3>COOLER LINES</h3>
    <div class="icon">
      <svg width="50" height="50" viewBox="0 0 50 50" aria-hidden="true"><g fill="none" stroke="#111" stroke-width="2.5"><circle cx="25" cy="25" r="13"/><circle cx="25" cy="25" r="8"/><circle cx="25" cy="25" r="3"/><path d="M25 38h14"/></g></svg>
    </div>
    <p>Maintaining optimal<br>engine temperature</p>
  </section>
  <section class="abs use-card card-fuel">
    <h3>OIL+FUEL HOSES</h3>
    <div class="icon">
      <svg width="50" height="50" viewBox="0 0 50 50" aria-hidden="true"><g fill="none" stroke="#111" stroke-width="2.5" stroke-linecap="round"><path d="M12 36c6-10 16-4 22-14"/><path d="M30 18l8-6"/><path d="M36 20l4 1M34 14l2-5"/></g></svg>
    </div>
    <p>Providing secure and<br>efficient fluid transfer</p>
  </section>

  <div class="abs call">Call Us: 0800 55 41 82</div>
  <div class="abs web">www.summitmotorworks.co.nz</div>
  <div class="abs email">Email:parts@summitmotorworks.co.nz</div>
  <div class="abs address">Address: 18 Marlow St, Eastfield, Hampton</div>
</main>
</body>
</html>
```